Dr. Martin Okelbrand
Chiropractic Physician
Simple
4817 Harwood Lane Suite B2
Miami Beach, Fl. 33127
(877) TU-VELAN (888-3526)
DrO@DrOkelbrand.example
www.DrOkelbrand.example
Im on PV, Plonkr, Wovel Net... So if someone has an Idea to throw something like that on there im up to check that out, THANKS! ALSO... I have another Toll Free number, (844)BRASK-OP. If someone wants to try it with that one in place of the TUVELAN number I would like to see which flows better on the card.
only the Dr. O logo that is attached i want to be large and on the back of the card

```html
<!DOCTYPE html>
<html lang="en">
<head>
<meta charset="utf-8">
<title>Dr. Martin Okelbrand – Business Card</title>
<link href="https://fonts.googleapis.com/css2?family=Open+Sans:wght@400;600;700&display=swap" rel="stylesheet">
<style>
  :root {
    --page-bg: #e9e6e2;
    --card-white: #ffffff;
    --brand-red: #c8102e;
    --ink-dark: #2e2e2e;
    --ink-grey: #6d6d6d;
    --text-on-red: #ffffff;
  }
  * { margin: 0; padding: 0; box-sizing: border-box; }
  html, body {
    width: 1200px; height: 646px; overflow: hidden;
    background: var(--page-bg);
    font-family: "Open Sans", Arial, sans-serif;
  }
  .canvas {
    position: relative; width: 1200px; height: 646px;
    display: flex; align-items: center; justify-content: center; gap: 60px;
  }
  .card {
    position: relative; width: 520px; height: 297px;
    background: var(--card-white);
    overflow: hidden;
    box-shadow: 0 6px 18px rgba(0,0,0,0.18);
  }
  .card-art { position: absolute; inset: 0; width: 100%; height: 100%; }

  /* Front: contact side */
  .contact-block {
    position: absolute; left: 24px; top: 28px;
    color: var(--text-on-red);
  }
  .contact-name { font-size: 16px; font-weight: 700; letter-spacing: 0.2px; }
  .contact-title { font-size: 11px; font-weight: 400; margin-top: 2px; opacity: 0.9; }
  .contact-address { font-size: 10.5px; line-height: 1.45; margin-top: 40px; font-style: normal; }
  .contact-lines { list-style: none; margin-top: 22px; font-size: 10.5px; line-height: 1.7; }
  .contact-lines li { display: flex; align-items: center; gap: 7px; }
  .contact-icon { width: 10px; height: 10px; flex: none; }

  /* Logo placeholder: invented name in one colour and weight */
  .logo-name {
    display: flex; align-items: center; gap: 8px;
    font-weight: 700; color: var(--ink-dark); line-height: 1.1; white-space: nowrap;
  }
  .logo-dot { border-radius: 50%; background: var(--brand-red); flex: none; }
  .logo-web { font-weight: 600; color: var(--ink-grey); white-space: nowrap; }

  .front-logo {
    position: absolute; right: 28px; top: 40px;
    display: flex; flex-direction: column; align-items: flex-end;
  }
  .front-logo .logo-name { font-size: 17px; }
  .front-logo .logo-dot { width: 10px; height: 10px; }
  .front-logo .logo-web { font-size: 9px; margin-top: 6px; }

  /* Back: logo side */
  .back-logo {
    position: absolute; inset: 0;
    display: flex; flex-direction: column; align-items: center; justify-content: center;
  }
  .back-logo .logo-name { font-size: 32px; gap: 12px; }
  .back-logo .logo-dot { width: 18px; height: 18px; }
  .back-logo .logo-web { font-size: 13px; margin-top: 12px; color: var(--ink-dark); }
</style>
</head>
<body>
<main class="canvas">

  <section class="card card-front" aria-label="Card front with contact details">
    <svg class="card-art" viewBox="0 0 520 297" aria-hidden="true">
      <defs>
        <linearGradient id="redPanel" x1="0" y1="0" x2="1" y2="1">
          <stop offset="0" stop-color="#d5152f"/>
          <stop offset="0.6" stop-color="#b00c24"/>
          <stop offset="1" stop-color="#7d0a1a"/>
        </linearGradient>
        <linearGradient id="greySwoosh" x1="0" y1="0" x2="1" y2="0">
          <stop offset="0" stop-color="#c4c4c4"/>
          <stop offset="1" stop-color="#7a7a7a"/>
        </linearGradient>
      </defs>
      <path d="M0,0 H218 C262,70 300,215 520,236 V297 H0 Z" fill="url(#greySwoosh)"/>
      <path d="M0,0 H206 C250,78 290,222 520,248 V297 H0 Z" fill="url(#redPanel)"/>
    </svg>

    <div class="contact-block">
      <p class="contact-name">Dr. Martin Okelbrand</p>
      <p class="contact-title">Chiropractic Physician</p>
      <address class="contact-address">
        4817 Harwood Lane Suite B2<br>
        Miami Beach, Fl. 33127
      </address>
      <ul class="contact-lines">
        <li>
          <svg class="contact-icon" viewBox="0 0 10 10"><path d="M2 0.5 L3.8 2.6 L2.8 3.6 C3.4 5 4.9 6.5 6.4 7.2 L7.4 6.2 L9.5 8 L8.2 9.5 C4.5 9.2 0.8 5.5 0.5 1.8 Z" fill="#fff"/></svg>
          (877) TU-VELAN (888-3526)
        </li>
        <li>
          <svg class="contact-icon" viewBox="0 0 10 10"><path d="M2 0.5 L3.8 2.6 L2.8 3.6 C3.4 5 4.9 6.5 6.4 7.2 L7.4 6.2 L9.5 8 L8.2 9.5 C4.5 9.2 0.8 5.5 0.5 1.8 Z" fill="#fff"/></svg>
          (844)BRASK-OP
        </li>
        <li>
          <svg class="contact-icon" viewBox="0 0 10 10"><rect x="0.5" y="2" width="9" height="6.5" fill="none" stroke="#fff"/><path d="M0.5 2 L5 5.6 L9.5 2" fill="none" stroke="#fff"/></svg>
          DrO@DrOkelbrand.example
        </li>
        <li>
          <svg class="contact-icon" viewBox="0 0 10 10"><circle cx="5" cy="5" r="4.3" fill="none" stroke="#fff"/><path d="M0.7 5 H9.3 M5 0.7 C2.8 3 2.8 7 5 9.3 M5 0.7 C7.2 3 7.2 7 5 9.3" fill="none" stroke="#fff" stroke-width="0.8"/></svg>
          www.DrOkelbrand.example
        </li>
      </ul>
    </div>

    <div class="front-logo">
      <div class="logo-name"><span>Dr. Martin Okelbrand</span><span class="logo-dot"></span></div>
      <p class="logo-web">www.DrOkelbrand.example</p>
    </div>
  </section>

  <section class="card card-back" aria-label="Card back with practice name">
    <div class="back-logo">
      <div class="logo-name"><span>Dr. Martin Okelbrand</span><span class="logo-dot"></span></div>
      <p class="logo-web">www.DrOkelbrand.example</p>
    </div>
  </section>

</main>
</body>
</html>
```